Business Cards Brimsworth Nuptials

I have a new webpage address and would like to update my business cards with Facebook and Instagram links as well. I need assistance with designing it. I have attached an old business card.

Target Market(s)

Potential couples wanting to get married and vendors who work with weddings

Industry/Entity Type

Wedding

Contact Information for Business Card

Name of Company (Brimsworth Nuptials), Pam Holcroft, Phone number (480-762-3038), Webpage: www.brimsworthnuptials4u.example, Facebook Link: Brimsworth Nuptials, Instagram Link: BrimsworthNuptials4u

Colors
0094D4
00A9DD
6FCCEA
C7EBF8
E9F6FB
00AB8E
00BBA5
67D7C9
C6EFE9
E9F9F6

Requirements
Nice to have
• Florals with teal on back of card. Not sure what needs to be on front and what on back
Should not have
• Definitive man/woman couple

```html
<!DOCTYPE html>
<html lang="en">
<head>
<meta charset="utf-8">
<title>Brimsworth Nuptials – Business Card</title>
<link rel="stylesheet" href="https://fonts.googleapis.com/css2?family=Poppins:wght@300;400;600;700&display=swap">
<style>
  :root {
    --stage: #2a2a2c;
    --card-white: #ffffff;
    --card-black: #111113;
    --sheen-dark: #151517;
    --sheen-mid: #242427;
    --sheen-light: #3a3a3e;
    --teal: #00939a;
    --ink: #151515;
  }
  * { margin: 0; padding: 0; box-sizing: border-box; }
  html, body {
    width: 1200px; height: 1108px; overflow: hidden;
    background: var(--stage);
    font-family: "Poppins", sans-serif;
  }
  .stage {
    position: relative; width: 1200px; height: 1108px;
    display: flex; justify-content: center; align-items: center; gap: 80px;
  }
  .card {
    width: 400px; height: 700px; border-radius: 22px;
    position: relative; overflow: hidden;
  }

  /* Front */
  .card-front { background: var(--card-white); color: var(--ink); }
  .brand {
    position: absolute; left: 48px; top: 150px; right: 40px;
    display: flex; align-items: center; gap: 16px;
  }
  .brand-dot {
    flex: none; width: 86px; height: 86px; border-radius: 50%; background: var(--teal);
  }
  .brand-name {
    font-weight: 700; font-size: 27px; line-height: 1.1; color: var(--ink);
    text-transform: uppercase; letter-spacing: 0.3px;
  }
  .person { position: absolute; left: 58px; top: 330px; }
  .person-name {
    font-weight: 600; font-size: 31px; line-height: 1.1;
    text-transform: uppercase; letter-spacing: 0.3px;
  }
  .person-title { font-size: 20px; font-weight: 300; line-height: 1.2; }
  .rule {
    position: absolute; left: 58px; top: 418px;
    width: 220px; height: 1.5px; background: var(--teal);
  }
  .phone {
    position: absolute; left: 0; right: 0; top: 432px; text-align: center;
    font-weight: 600; font-size: 42px; letter-spacing: 1px; line-height: 1.2;
  }
  .icon-row {
    position: absolute; left: 0; right: 0; top: 510px;
    display: flex; justify-content: center; align-items: center; gap: 8px;
  }
  .icon-row .line { width: 44px; height: 1.5px; background: var(--teal); }
  .icon {
    width: 26px; height: 26px; border-radius: 50%; background: var(--teal);
    display: flex; align-items: center; justify-content: center;
  }
  .links {
    position: absolute; left: 0; right: 0; top: 548px; text-align: center;
    font-size: 16px; line-height: 1.5;
  }

  /* Back */
  .card-back { background: var(--card-black); }
  .back-pattern {
    position: absolute; inset: 0;
    background:
      radial-gradient(ellipse 75% 55% at 90% 12%, var(--sheen-light), transparent 70%),
      radial-gradient(ellipse 60% 45% at 70% 55%, var(--sheen-mid), transparent 75%),
      linear-gradient(160deg, var(--sheen-mid) 0%, var(--sheen-dark) 55%, var(--card-black) 100%);
  }
  .back-mark {
    position: absolute; left: 200px; top: 500px;
    display: flex; align-items: center; gap: 8px;
    font-weight: 600; font-size: 14px; color: var(--teal); white-space: nowrap;
  }
  .back-mark .brand-dot { width: 30px; height: 30px; }
</style>
</head>
<body>
<main class="stage">
  <section class="card card-front" aria-label="Business card front">
    <div class="brand">
      <span class="brand-name">Brimsworth<br>Nuptials 4U</span>
      <span class="brand-dot"></span>
    </div>
    <div class="person">
      <p class="person-name">Pam Holcroft</p>
      <p class="person-title">Wedding officiant</p>
    </div>
    <div class="rule"></div>
    <p class="phone">480-762-3038</p>
    <div class="icon-row">
      <span class="line"></span>
      <span class="icon">
        <svg width="16" height="16" viewBox="0 0 16 16" fill="none" stroke="#fff" stroke-width="1.3">
          <circle cx="8" cy="8" r="6.5"/><ellipse cx="8" cy="8" rx="3" ry="6.5"/><line x1="1.5" y1="8" x2="14.5" y2="8"/>
        </svg>
      </span>
      <span class="icon"></span>
      <span class="icon"></span>
      <span class="line"></span>
    </div>
    <p class="links">www.brimsworthnuptials4u.example<br>Brimsworth Nuptials<br>BrimsworthNuptials4u</p>
  </section>

  <section class="card card-back" aria-label="Business card back">
    <div class="back-pattern" role="img" aria-label="Embossed repeating pattern of hearts and roses in glossy black"></div>
    <div class="back-mark">
      <span class="brand-dot"></span>
      <span>Brimsworth Nuptials</span>
    </div>
  </section>
</main>
</body>
</html>
```